KRV Inc Web Design

WHAT ARE WE DOING?
We are developing a new website look and feel for a new company called KRV Inc. This new look and feel should include colors, design elements, choice of photography and other imagery, fonts, and other user experience elements.

WHAT DO THEY DO?
KRV, Inc, makes tools for researchers who are studying protein-protein interactions. These molecules are the basic tools of biology, and serve as key targets for drug developers and disease researchers. The world of proteins is enormously complex, and companies like KRV provide researchers with critical tools that help them elucidate this world.

WHO ARE WE TALKING TO?
The target audience for this website are professional scientists working in university research or biopharma drug development. They are highly sophisticated consumers looking for key tools that will advance their research.

WHAT DO WE WANT THEM TO DO?
The site is an information resource for the customer exploring the tools that KRV sells and the scientific issues surrounding protein-protein interactions. They should be able to navigate easily to their content of choice, while the whole site should convey a professionalism that enhanced KRV’s credibility.

WHAT DOES THE KRV BRAND STAND FOR?
KRV stands for illumination. Proteins are challenging to study, and KRV exists to help shed light on their workings.

WHAT ARE THE KEY VALUES OF THE KRV BRAND?
Integrity. Innovation. Insight.

WHAT ARE THE EXECUTIONAL MANDITORIES?
The look and feel is completely up for grabs. Nothing is off the table.

WHAT ARE THE DELIVERABLES?
We need new designs for the following templates:
http://cms.thevormelgroup.com/
http://cms.thevormelgroup.com/products-and-services/instruments-3/bench-top-instruments/
http://cms.thevormelgroup.com/category/lab-study/

```html
<!DOCTYPE html>
<html lang="en">
<head>
<meta charset="utf-8">
<title>KRV Inc – Bench Top Instruments</title>
<link href="https://fonts.googleapis.com/css2?family=Oswald:wght@300;400&family=Arimo:wght@400;700&family=Open+Sans:wght@400&display=swap" rel="stylesheet">
<style>
  :root {
    --brand-orange: #f9b03f;
    --link-orange: #e8872a;
    --nav-active: #646464;
    --ink: #555555;
    --ink-dark: #333333;
    --muted: #6d6d6d;
    --rule: #a8a8a8;
    --field-bg: #eeeeee;
    --footer-bg: #646464;
    --white: #ffffff;
    --photo-lab: #c9d3df;
    --photo-lab-deep: #8fa0b4;
    --photo-unit: #dde3ea;
  }
  * { box-sizing: border-box; margin: 0; padding: 0; }
  html, body { width: 1167px; height: 1200px; overflow: hidden; background: var(--white); }
  body { position: relative; font-family: "Arimo", Arial, sans-serif; color: var(--ink); }
  a { color: inherit; text-decoration: none; }

  .brand {
    position: absolute; left: 50px; top: 20px;
    font-family: "Oswald", sans-serif; font-weight: 300;
    font-size: 64px; letter-spacing: 14px; line-height: 70px; color: var(--muted);
  }
  .utility-links {
    position: absolute; right: 36px; top: 28px;
    font-family: "Open Sans", sans-serif; font-size: 12px; color: var(--muted); letter-spacing: .3px;
  }
  .utility-links span { margin: 0 6px; }
  .search {
    position: absolute; left: 728px; top: 54px; width: 403px; height: 34px;
    background: var(--field-bg); border: 1px solid var(--rule); border-radius: 5px;
    font-family: "Oswald", sans-serif; font-weight: 300; font-size: 17px; color: var(--ink-dark);
    line-height: 32px; padding-left: 14px;
  }
  .search svg { position: absolute; right: 12px; top: 6px; }

  .main-nav {
    position: absolute; left: 0; top: 118px; width: 1167px; height: 55px;
    background: var(--brand-orange); font-family: "Oswald", sans-serif; font-weight: 300;
    font-size: 23px; color: var(--white); text-transform: uppercase;
  }
  .main-nav a { position: absolute; top: 0; height: 55px; line-height: 55px; }
  .main-nav .is-active { background: var(--nav-active); padding: 0 36px; }

  .breadcrumb {
    position: absolute; left: 280px; top: 194px;
    font-family: "Open Sans", sans-serif; font-size: 13px; color: var(--muted);
  }

  .side-nav { position: absolute; left: 0; top: 234px; width: 192px; text-align: right; font-size: 16px; color: var(--ink); }
  .side-nav h3 { font-size: 16px; font-weight: 700; color: var(--ink-dark); line-height: 19px; margin-bottom: 36px; }
  .side-nav li { list-style: none; line-height: 20px; margin-bottom: 8px; }
  .side-nav .current { color: var(--ink-dark); margin-right: -12px; }
  .side-nav .current::after { content: ""; display: inline-block; margin-left: 5px; border-left: 6px solid var(--ink-dark); border-top: 5px solid transparent; border-bottom: 5px solid transparent; }

  .page-title { position: absolute; left: 277px; top: 229px; font-size: 29px; font-weight: 400; color: var(--ink-dark); }

  .intro { position: absolute; left: 277px; top: 292px; width: 846px; font-size: 16.5px; line-height: 24px; color: var(--ink); }
  .intro p { margin-bottom: 24px; }
  .intro .accent { color: var(--link-orange); }
  .hero-photo {
    float: left; width: 357px; height: 238px; margin: 0 33px 8px 0;
    background: linear-gradient(135deg, var(--photo-lab) 0%, #e9eef4 45%, var(--photo-lab-deep) 100%);
  }

  .tabs { position: absolute; left: 290px; top: 668px; height: 46px; z-index: 2; }
  .tab {
    position: absolute; top: 0; height: 46px; line-height: 45px; text-align: center;
    border: 1px solid var(--rule); border-bottom: none; border-radius: 5px 5px 0 0;
    background: var(--white); font-family: "Open Sans", sans-serif; font-size: 17px; color: var(--ink);
  }
  .tab.is-active { background: var(--rule); color: var(--white); border-color: var(--rule); height: 47px; }

  .tab-panel {
    position: absolute; left: 269px; top: 713px; width: 845px; height: 349px;
    border: 2px solid var(--rule); border-radius: 11px; padding: 28px 27px 0 29px;
    font-size: 16.5px; line-height: 24px; color: var(--ink);
  }
  .tab-panel p { margin-bottom: 24px; }
  .unit-photo {
    float: right; width: 238px; height: 159px; margin: 0 0 8px 30px;
    background: linear-gradient(160deg, #f1f4f7 0%, var(--photo-unit) 55%, var(--photo-lab-deep) 100%);
  }

  .site-footer {
    position: absolute; left: 0; top: 1107px; width: 1167px; height: 93px;
    background: var(--footer-bg); color: var(--white);
    font-family: "Open Sans", sans-serif; font-size: 14.5px;
  }
  .footer-links { position: absolute; left: 35px; top: 24px; }
  .footer-links a { margin-right: 12px; }
  .social { position: absolute; left: 797px; top: 19px; display: flex; gap: 22px; }
  .social span { width: 31px; height: 31px; border-radius: 50%; background: var(--white); display: block; }
  .copyright { position: absolute; right: 44px; top: 24px; }
</style>
</head>
<body>
  <header>
    <div class="brand">KRV INC</div>
    <nav class="utility-links"><a href="#">SITEMAP</a><span>|</span><a href="#">CONTACT US</a></nav>
    <div class="search">ENTER KEYWORD
      <svg width="24" height="22" viewBox="0 0 24 22" aria-hidden="true"><circle cx="9" cy="8" r="6.5" fill="none" stroke="#555" stroke-width="2.5"/><line x1="14" y1="13" x2="22" y2="20" stroke="#555" stroke-width="4" stroke-linecap="round"/></svg>
    </div>
  </header>

  <nav class="main-nav">
    <a href="#" style="left:54px">Company</a>
    <a href="#" class="is-active" style="left:169px">Products &amp; Services</a>
    <a href="#" style="left:461px">Learning Center</a>
    <a href="#" style="left:676px">Events</a>
    <a href="#" style="left:806px">KRV News</a>
    <a href="#" style="left:958px">Contact Us</a>
  </nav>

  <div class="breadcrumb">Home » Products &amp; Services » Instruments » Bench Top Instruments</div>

  <aside class="side-nav">
    <h3>PRODUCTS<br>OVERVIEW</h3>
    <ul>
      <li>INSTRUMENTS</li>
      <li class="current">Bench Top Instruments</li>
      <li>Microscope<br>Attachments</li>
    </ul>
  </aside>

  <h1 class="page-title">Bench Top Instruments</h1>

  <section class="intro">
    <div class="hero-photo" role="img" aria-label="Automated laboratory bench instrument with robotic arm and sample tray"></div>
    <p>Maecenas imperdiet nisi eu justo dapibus, commodo <span class="accent">venenatis massa tempus</span>. Morbi consectetur sed justo vitae dictum. Ut semper tincidunt accumsan.</p>
    <p>Nunc suscipit dui in massa ultricies, ac sagittis velit pulvinar. In scelerisque id lectus eu facilisis. <span class="accent">Morbi et nunc non nulla</span> lobortis ultricies sit amet a turpis. Integer eget ullamcorper metus.</p>
    <p>Cras vitae nibh non dolor scelerisque porta.Nunc suscipit dui in massa ultricies, ac sagittis velit pulvinar. In scelerisque id lectus eu facilisis. <span class="accent">Morbi et nunc non nulla</span> lobortis ultricies sit amet a turpis. Integer eget ullamcorper metus.</p>
  </section>

  <div class="tabs">
    <div class="tab is-active" style="left:0;width:129px">Overview</div>
    <div class="tab" style="left:132px;width:129px">Features</div>
    <div class="tab" style="left:265px;width:163px">Specifications</div>
    <div class="tab" style="left:431px;width:99px">FAQ’s</div>
    <div class="tab" style="left:533px;width:123px">Manuals</div>
  </div>

  <section class="tab-panel">
    <div class="unit-photo" role="img" aria-label="Compact white bench top instrument with small display screen"></div>
    <p>Donec nec ipsum eget erat lacinia consectetur. Sed non turpis pretium, porttitor lorem eu, congue turpis. Vivamus viverra semper sem eget elementum. Aliquam augue libero, hendrerit a tortor vestibulum, rutrum suscipit ante. Curabitur a ligula ligula. In eget eros non metus elementum consequat id quis enim.</p>
    <p>Vivamus dignissim pharetra mi a tempor. Aenean pellentesque, arcu sed sodales vestibulum, nunc nulla molestie sem, ut imperdiet neque turpis sed purus. Nunc euismod tortor nec nibh venenatis convallis. Suspendisse magna augue, blandit et quam ac, fermentum dignissim purus. Curabitur tempor ac metus ut bibendum. Nulla id nisi semper, ornare nisi quis, laoreet dolor. Aliquam erat volutpat. Suspendisse ac metus sed orci mattis tempor ut eu lectus.</p>
  </section>

  <footer class="site-footer">
    <nav class="footer-links">
      <a href="#">Home</a><a href="#">Company</a><a href="#">Products &amp; Services</a><a href="#">Contact Us</a><a href="#">Site Map</a><a href="#">Privacy Policy</a><a href="#">Terms</a>
    </nav>
    <div class="social"><span role="img" aria-label="Social profile link"></span><span role="img" aria-label="Social profile link"></span></div>
    <div class="copyright">© 2013 KRV INC</div>
  </footer>
</body>
</html>
```